Powerpoint template
Zielgruppe
Scientific research, novel molecule discovery & development”
Aufgabenstellung
Design of a template in the 16:9 aspect ratio - this will be used to create an interactive pdf employing indesign creative software.
The template should include options for opening slides , transition slides , and also closing slides.
Overall the design should be 'clean , neat and with lots of white space' - here the website of a similar company to ours which represents a direction in terms of design that approximates what we would like our final interactive pdf to look like. https://torvexlab.co/
As guidance please refer to the enclosed document with 3 design options that were created by a freelance designer working with the company-the first example is probably the closest to what we would like but we are not exactly satisfied with this example. The black lettering also is too dominant and not appropriate.
The last option is very much 'business focused' and such a design could be considered if the theme is more scientific rather than business orientated. The second example we consider inappropriate and too 'traditional' and not modern enough at all.

```html
<!DOCTYPE html>
<html lang="en">
<head>
<meta charset="utf-8">
<title>Cerevane Biopharma – Presentation Template</title>
<link rel="stylesheet" href="https://fonts.googleapis.com/css2?family=Rubik:wght@500;700&family=Roboto:wght@300;400&display=swap">
<style>
  :root {
    --ink: #27234f;
    --ink-soft: #3a3660;
    --bg-warm: #f8efed;
    --bg-cool: #d6d1e2;
    --panel-light: rgba(255,255,255,0.18);
    --wave-a: #c9bfe0;
    --wave-b: #e6d7e6;
    --molecule: #7fb2dc;
    --divider: #8a86a8;
    --footer: rgba(255,255,255,0.85);
  }
  * { box-sizing: border-box; margin: 0; padding: 0; }
  html, body { width: 1200px; height: 2702px; overflow: hidden; background: #ffffff; }
  body { font-family: "Roboto", Arial, sans-serif; color: var(--ink); }

  .slide {
    position: relative;
    width: 1200px;
    height: 675px;
    overflow: hidden;
    background: linear-gradient(100deg, var(--bg-warm) 0%, #e9e2ea 55%, var(--bg-cool) 100%);
  }
  .slide + .slide { margin-top: 0.67px; }

  .decor {
    position: absolute;
    background:
      radial-gradient(ellipse at 55% 45%, rgba(190,178,222,0.55) 0%, rgba(214,205,232,0.25) 45%, rgba(255,255,255,0) 75%),
      radial-gradient(circle at 22% 20%, rgba(127,178,220,0.28) 0%, rgba(127,178,220,0) 35%),
      radial-gradient(circle at 35% 85%, rgba(127,178,220,0.25) 0%, rgba(127,178,220,0) 35%);
  }

  .heading {
    font-family: "Rubik", Arial, sans-serif;
    font-weight: 700;
    color: var(--ink);
    text-align: center;
    position: absolute;
  }
  .body-copy {
    font-family: "Roboto", Arial, sans-serif;
    font-weight: 300;
    color: var(--ink);
    text-align: center;
    position: absolute;
  }

  /* Slide 1 – opening */
  .opening .decor { left: 0; top: 0; width: 629px; height: 675px; }
  .opening .side-panel { position: absolute; left: 629px; top: 0; width: 571px; height: 675px; background: var(--panel-light); }
  .opening .brand { left: 629px; width: 480px; top: 228px; font-size: 52px; line-height: 54px; letter-spacing: 1px; }
  .opening .tagline { left: 629px; width: 480px; top: 368px; font-size: 31px; line-height: 37px; }

  /* Slide 2 – transition */
  .vision .decor { left: 0; top: 0; width: 246px; height: 675px; }
  .vision .heading { left: 0; width: 1200px; top: 182px; font-size: 48px; }
  .vision .body-copy { left: 0; width: 1200px; top: 322px; font-size: 28px; line-height: 37px; }

  .slide-footer {
    position: absolute; left: 94px; top: 614px;
    font-size: 13px; color: var(--footer); font-weight: 400;
  }
  .footer-brand {
    position: absolute; left: 1018px; top: 606px;
    font-size: 13px; line-height: 14px; color: var(--footer); font-weight: 400;
  }

  /* Slide 3 – content */
  .problem .heading { left: 0; width: 1200px; top: 106px; font-size: 50px; }
  .stat { position: absolute; top: 302px; width: 230px; text-align: center; }
  .stat-title { font-family: "Rubik", Arial, sans-serif; font-weight: 500; font-size: 21px; letter-spacing: 0.5px; color: var(--ink-soft); }
  .stat-icon { display: block; margin: 20px auto 0; width: 60px; height: 76px; border-radius: 6px; background: linear-gradient(180deg, #3a3163, #27234f); opacity: 0.9; }
  .stat-text { margin-top: 30px; font-size: 14px; line-height: 18.5px; font-weight: 300; color: var(--ink); }
  .divider { position: absolute; top: 304px; width: 1px; height: 238px; background: var(--divider); opacity: 0.7; }

  /* Slide 4 – closing */
  .closing .decor { left: 620px; top: 0; width: 580px; height: 675px; }
  .closing .brand { left: 110px; width: 500px; top: 108px; font-family: "Rubik", Arial, sans-serif; font-weight: 500; font-size: 57px; line-height: 58px; letter-spacing: 1px; }
  .closing .thanks { left: 110px; width 500px; width: 500px; top: 358px; font-size: 46px; }
  .closing .contact { left: 110px; width: 500px; top: 448px; font-size: 28px; line-height: 37px; font-weight: 400; }
</style>
</head>
<body>

<section class="slide opening">
  <div class="decor" role="img" aria-label="Flowing lavender line-wave ribbon with blue hexagonal molecule structures"></div>
  <div class="side-panel"></div>
  <h1 class="heading brand">CEREVANE<br>BIOPHARMA</h1>
  <p class="body-copy tagline">A global leader in pioneering<br>research, novel molecule<br>discovery and development</p>
</section>

<section class="slide vision">
  <div class="decor" role="img" aria-label="Flowing lavender line-wave ribbon"></div>
  <h2 class="heading">Our Vision</h2>
  <p class="body-copy">Setting the standards through collaborative development,<br>applied research and superlative in-house experience<br>in extraction and characterization of natural psilocybin for<br>disease modifying mental health treatments.</p>
  <div class="slide-footer">02 | Our Vision</div>
  <div class="footer-brand">CEREVANE<br>BIOPHARMA</div>
</section>

<section class="slide problem">
  <h2 class="heading">Problem: Clinical Depression</h2>

  <div class="stat" style="left:86px">
    <div class="stat-title">AGE</div>
    <span class="stat-icon" role="img" aria-label="Hourglass icon"></span>
    <p class="stat-text">Major depressive disorder affects approximately 17.3 million American adults, or about 7.1% of the U.S. population age 18 and older, in a given year.</p>
  </div>
  <div class="divider" style="left:350px"></div>

  <div class="stat" style="left:375px">
    <div class="stat-title">HEALTH</div>
    <span class="stat-icon" role="img" aria-label="Anatomical heart icon"></span>
    <p class="stat-text">Adults with a depressive disorder or symptoms have a 64% greater risk of developing coronary artery disease.</p>
  </div>
  <div class="divider" style="left:630px"></div>

  <div class="stat" style="left:641px">
    <div class="stat-title">GENDER</div>
    <span class="stat-icon" role="img" aria-label="Woman and man figures icon"></span>
    <p class="stat-text">Major depressive disorder<br>is more prevalent in<br>women than in men.</p>
  </div>
  <div class="divider" style="left:881px"></div>

  <div class="stat" style="left:899px">
    <div class="stat-title">CHILDREN</div>
    <span class="stat-icon" role="img" aria-label="Child holding a balloon icon"></span>
    <p class="stat-text">1.9 million children, 3–17,<br>have diagnosed depression.</p>
  </div>

  <div class="slide-footer">03 | Problem: Clinical Depression</div>
  <div class="footer-brand">CEREVANE<br>BIOPHARMA</div>
</section>

<section class="slide closing">
  <div class="decor" role="img" aria-label="Flowing lavender line-wave ribbon with blue hexagonal molecule structures"></div>
  <h2 class="heading brand">CEREVANE<br>BIOPHARMA</h2>
  <h3 class="heading thanks">Thank you!</h3>
  <p class="body-copy contact">www.cerevanebiopharma.com<br>+44 020 7946 0321<br>e-mail adresse</p>
</section>

</body>
</html>
```